Business Card Design Project

i have the logo designed.
I require designs for the managing director and the general manager.
we need space for email, and a mobile number.
any other cool stuff/design you guys just let me see what you got.
The managing director card could be black, minimalist, and the cards for the rest of the company could be using the green logo.
it has to impress. transportation market is fragmented, we want to appear professional and sophisticated.
Md: Tarek bani rahim
General manager: omer rahim
clients: procurement heads of contracting companies
Business

```html
<!DOCTYPE html>
<html lang="en">
<head>
<meta charset="utf-8">
<title>Veloxa Business Card – Front and Back</title>
<link rel="stylesheet" href="https://fonts.googleapis.com/css2?family=Exo+2:wght@300;400;600;700&display=swap">
<style>
  :root {
    --page-bg: #e9e9e6;
    --card-charcoal: #3a3b3e;
    --card-charcoal-deep: #2c2d30;
    --green-bright: #3fbf3a;
    --green-mid: #2ea52c;
    --green-deep: #1d7f22;
    --text-white: #f2f2f2;
    --text-muted: #b9bcbf;
    --divider: #5a5c60;
  }
  * { box-sizing: border-box; margin: 0; padding: 0; }
  html, body { width: 849px; height: 1200px; overflow: hidden; }
  body {
    background: var(--page-bg);
    font-family: "Exo 2", Arial, sans-serif;
    display: flex;
    flex-direction: column;
    align-items: center;
    justify-content: center;
    gap: 90px;
  }
  .card {
    position: relative;
    width: 700px;
    height: 400px;
    background: linear-gradient(135deg, var(--card-charcoal) 0%, var(--card-charcoal-deep) 100%);
    overflow: hidden;
    box-shadow: 0 10px 30px rgba(0,0,0,0.25);
  }
  .card-shapes { position: absolute; inset: 0; width: 100%; height: 100%; }
  .card-content { position: absolute; inset: 0; }

  /* Front */
  .identity {
    position: absolute;
    right: 380px;
    top: 150px;
    text-align: right;
    text-transform: uppercase;
  }
  .identity-first {
    color: var(--text-white);
    font-size: 34px;
    font-weight: 600;
    letter-spacing: 2px;
    line-height: 1;
  }
  .identity-last {
    color: var(--green-bright);
    font-size: 34px;
    font-weight: 600;
    letter-spacing: 2px;
    line-height: 1.1;
  }
  .identity-role {
    color: var(--text-muted);
    font-size: 12px;
    letter-spacing: 1.5px;
    margin-top: 8px;
    line-height: 1.4;
  }
  .divider {
    position: absolute;
    left: 340px;
    top: 140px;
    width: 1px;
    height: 120px;
    background: var(--divider);
  }
  .contact {
    position: absolute;
    left: 362px;
    top: 148px;
    text-transform: uppercase;
  }
  .contact-item + .contact-item { margin-top: 22px; }
  .contact-label {
    color: var(--green-bright);
    font-size: 12px;
    font-weight: 600;
    letter-spacing: 1.5px;
    display: flex;
    align-items: center;
    gap: 6px;
  }
  .contact-label svg { width: 12px; height: 12px; }
  .contact-value {
    color: var(--text-white);
    font-size: 17px;
    font-weight: 300;
    letter-spacing: 1px;
    margin-top: 4px;
  }

  /* Back */
  .brand {
    position: absolute;
    inset: 0;
    display: flex;
    align-items: center;
    justify-content: center;
    gap: 18px;
  }
  .brand-dot {
    width: 46px;
    height: 46px;
    border-radius: 50%;
    background: var(--green-bright);
  }
  .brand-name {
    color: var(--green-bright);
    font-size: 64px;
    font-weight: 600;
    letter-spacing: 1px;
  }
</style>
</head>
<body>

  <section class="card card-front" aria-label="Card front">
    <svg class="card-shapes" viewBox="0 0 700 400" aria-hidden="true">
      <polygon points="470,0 700,0 700,170" fill="var(--green-mid)"/>
      <polygon points="540,0 700,0 700,90" fill="var(--green-bright)"/>
      <polygon points="0,0 170,0 0,120" fill="var(--green-deep)"/>
      <polygon points="0,250 0,400 210,400" fill="var(--green-mid)"/>
      <polygon points="0,320 0,400 110,400" fill="var(--green-bright)"/>
      <polygon points="560,400 700,300 700,400" fill="var(--green-deep)"/>
    </svg>
    <div class="card-content">
      <div class="identity">
        <p class="identity-first">Tarek</p>
        <p class="identity-last">Bani Rahim</p>
        <p class="identity-role">Managing Director<br>(GM: Omer Rahim)</p>
      </div>
      <div class="divider"></div>
      <div class="contact">
        <div class="contact-item">
          <p class="contact-label">Phone
            <svg viewBox="0 0 12 12"><path d="M3 1l2 2.5-1.2 1.3a6 6 0 0 0 3.4 3.4L8.5 7 11 9l-1 2C5 11 1 7 1 2z" fill="currentColor"/></svg>
          </p>
          <p class="contact-value">+90 555 010 0199</p>
        </div>
        <div class="contact-item">
          <p class="contact-label">E-mail
            <svg viewBox="0 0 12 12"><rect x="1" y="2.5" width="10" height="7" fill="none" stroke="currentColor" stroke-width="1.2"/><path d="M1 3l5 3.5L11 3" fill="none" stroke="currentColor" stroke-width="1.2"/></svg>
          </p>
          <p class="contact-value">info@veloxa.com</p>
        </div>
      </div>
    </div>
  </section>

  <section class="card card-back" aria-label="Card back">
    <svg class="card-shapes" viewBox="0 0 700 400" aria-hidden="true">
      <polygon points="430,0 700,0 700,150" fill="var(--green-mid)"/>
      <polygon points="520,0 700,0 700,70" fill="var(--green-bright)"/>
      <polygon points="0,0 200,0 0,150" fill="var(--green-deep)"/>
      <polygon points="0,230 0,400 240,400" fill="var(--green-mid)"/>
      <polygon points="0,310 0,400 120,400" fill="var(--green-bright)"/>
      <polygon points="540,400 700,280 700,400" fill="var(--green-mid)"/>
    </svg>
    <div class="brand">
      <span class="brand-dot" aria-hidden="true"></span>
      <span class="brand-name">Veloxa</span>
    </div>
  </section>

</body>
</html>
```